Modern, corporate management consultancy firm needs a new website

We need a website for an Australian based management consultancy firm.

The company name is Corbel Strategy Partners.

We are looking for a parallax style wordpress site.

The site needs to provide the following functions:

1) subscribe function
2) links to social media (twitter, linkedin and mail)
3) a gated document section where people can download pdf's from the site after registering or providing name, company, position, email and contact number.

Attached is the company logo, would like to see designs that incorporate the dark blue and silver in the logo and separated into the following sections (Home, About, Services (with 4 options), Our Team, Links, Contacts.

Need the site to be easy to navigate and updated.

Potentially a News Section that can be updated regularly.

Target Market(s)

Target market is SME, business owners and directors

Industry/Entity Type

Management Consulting

Coding

Coded - Design and coding required

Number of Pages Required

1 page

Font styles to use
Sans Serif

Colors
0255a3
cbcbcb
757575
000000

Requirements
Must have
• Must be easy to read and use
Nice to have
• Features are listed on initial brief

```html
<!DOCTYPE html>
<html lang="en">
<head>
<meta charset="utf-8">
<title>Corbel Strategy Partners – Business Improvement Specialists</title>
<link rel="stylesheet" href="https://fonts.googleapis.com/css2?family=Open+Sans:wght@400;600;700;800&display=swap">
<style>
:root{
  --blue:#0255a3;
  --navy:#1c3553;
  --navy-dark:#152a43;
  --silver:#cbcbcb;
  --grey:#757575;
  --ink:#2a2a2a;
  --band:#eef0f3;
  --red:#d9443a;
  --white:#ffffff;
}
*{box-sizing:border-box;margin:0;padding:0}
html,body{width:1200px;height:2672px;overflow:hidden}
body{font-family:"Open Sans",Arial,sans-serif;color:var(--ink);background:var(--white);position:relative}
section,header,footer{position:absolute;left:0;width:1200px}
.section-title{font-size:30px;font-weight:600;color:var(--navy);text-align:center}
.lead{font-size:12px;line-height:20px;color:var(--grey);text-align:center}

/* header */
.site-header{top:0;height:64px;background:var(--white);z-index:3;display:flex;align-items:center;padding:0 60px}
.brand{display:flex;align-items:center;gap:12px}
.brand-dot{width:34px;height:34px;border-radius:50%;background:var(--navy)}
.brand-name{font-size:17px;font-weight:600;color:var(--navy)}
.main-nav{margin-left:auto;display:flex;gap:36px;align-items:center}
.main-nav a{font-size:12px;font-weight:600;color:var(--navy);text-decoration:none;letter-spacing:.5px;padding:22px 0}
.main-nav a.active{color:var(--blue);border-bottom:3px solid var(--blue)}

/* hero */
.hero{top:64px;height:520px;overflow:hidden}
.hero-photo{position:absolute;inset:0;background:linear-gradient(180deg,#7fb4de 0%,#a9cde9 45%,#5d87ad 75%,#34597d 100%)}
.hero-copy{position:absolute;left:100px;top:170px;width:600px;color:var(--white)}
.hero-copy h1{font-size:44px;line-height:50px;font-weight:800;color:var(--navy);text-transform:uppercase}
.hero-copy p{margin-top:18px;font-size:13px;line-height:20px;color:var(--white);font-weight:600}
.btn-more{display:inline-block;margin-top:26px;background:var(--navy);color:var(--white);font-size:12px;font-weight:700;padding:12px 22px;letter-spacing:.5px}
.hero-arrow{position:absolute;top:240px;width:26px;height:40px}
.hero-slant{position:absolute;left:0;bottom:0}

/* about */
.about{top:600px;height:280px;text-align:center}
.about .section-title{margin-top:20px}
.about .lead{width:760px;margin:26px auto 0}

/* services */
.services{top:880px;height:370px;background:var(--band)}
.services .section-title{margin-top:36px}
.services .lead{width:760px;margin:14px auto 0}
.service-list{display:flex;justify-content:center;gap:70px;margin-top:32px}
.service{width:190px;text-align:center}
.service-icon{width:76px;height:76px;border-radius:50%;border:2px solid var(--navy);margin:0 auto;display:flex;align-items:center;justify-content:center;background:var(--white)}
.service-icon.active{background:var(--navy)}
.service h3{font-size:13px;font-weight:700;color:var(--navy);margin-top:16px}
.service p{font-size:11px;line-height:17px;color:var(--grey);margin-top:8px}
.services-arrow{position:absolute;top:200px}

/* news & links */
.news-links{top:1250px;height:330px;display:flex;padding:30px 100px 0}
.news,.links{width:500px}
.links{margin-left:30px}
.col-title{font-size:26px;font-weight:600;color:var(--navy);margin-bottom:18px}
.news-item{margin-bottom:22px}
.news-item h4{font-size:12px;font-weight:700;color:var(--navy)}
.news-item p{font-size:11px;line-height:17px;color:var(--grey);margin-top:6px}
.news-item .more{font-size:11px;color:var(--blue);margin-top:4px}
.links h4{font-size:12px;font-weight:700;color:var(--navy);margin-bottom:10px}
.link-row{font-size:11px;line-height:24px;color:var(--grey)}
.link-row span{color:var(--blue);text-decoration:underline;margin-right:8px}

/* team */
.team{top:1580px;height:540px;background:var(--white)}
.team .section-title{margin-top:20px}
.team .lead{margin-top:12px}
.team-list{display:flex;justify-content:center;gap:70px;margin-top:36px}
.member{width:280px;text-align:center}
.member-photo{width:280px;height:190px}
.member h3{font-size:20px;font-weight:600;color:var(--navy);margin-top:18px}
.member p{font-size:11px;line-height:17px;color:var(--grey);margin-top:10px}
.social{display:flex;justify-content:center;gap:8px;margin-top:14px}
.social span{width:24px;height:24px;border-radius:50%;background:var(--blue)}
.social span.mail{background:var(--red);display:flex;align-items:center;justify-content:center}

/* contact */
.contact{top:2120px;height:440px;background:var(--navy);color:var(--white);text-align:center}
.contact .section-title{color:var(--white);margin-top:34px}
.contact-details{font-size:13px;line-height:22px;margin-top:14px}
.contact-form{display:flex;gap:40px;justify-content:center;margin-top:26px}
.field-message{width:420px;height:190px;background:var(--white);text-align:left;font-size:11px;color:var(--grey);padding:10px}
.fields{width:400px;display:flex;flex-direction:column;gap:14px}
.field{height:40px;background:var(--white);font-size:11px;color:var(--grey);text-align:left;padding:12px 10px}
.field-row{display:flex;gap:14px}
.field-row .field{flex:1}
.btn-submit{width:130px;height:40px;background:var(--navy-dark);border:1px solid #3f5a7a;color:var(--white);font-size:12px;font-weight:700;display:flex;align-items:center;justify-content:center;letter-spacing:.5px}

/* footer */
.site-footer{top:2560px;height:112px;text-align:center}
.to-top{position:absolute;left:582px;top:-18px;width:36px;height:36px;border-radius:50%;background:var(--navy);display:flex;align-items:center;justify-content:center}
.copyright{font-size:11px;color:var(--grey);margin-top:52px}
.copyright b{color:var(--blue);font-weight:600}
</style>
</head>
<body>

<header class="site-header">
  <div class="brand"><span class="brand-dot"></span><span class="brand-name">Corbel Strategy Partners</span></div>
  <nav class="main-nav">
    <a class="active" href="#">HOME</a><a href="#">ABOUT</a><a href="#">SERVICES</a><a href="#">OUR TEAM</a><a href="#">CONTACTS</a>
    <svg width="14" height="14" viewBox="0 0 14 14"><circle cx="6" cy="6" r="4.5" fill="none" stroke="#1c3553" stroke-width="2"/><line x1="9.5" y1="9.5" x2="13" y2="13" stroke="#1c3553" stroke-width="2"/></svg>
  </nav>
</header>

<section class="hero">
  <div class="hero-photo" role="img" aria-label="City skyline with tall towers under a blue sky"></div>
  <svg class="hero-arrow" style="left:20px" viewBox="0 0 26 40"><polyline points="20,6 6,20 20,34" fill="none" stroke="#fff" stroke-width="3"/></svg>
  <svg class="hero-arrow" style="right:20px" viewBox="0 0 26 40"><polyline points="6,6 20,20 6,34" fill="none" stroke="#fff" stroke-width="3"/></svg>
  <div class="hero-copy">
    <h1>Business Improvement<br>Specialists</h1>
    <p>Statement of intent – Providing tailored practical advice to businesses, working together to identify problems areas, resolve issues and improve performance.</p>
    <span class="btn-more">READ MORE</span>
  </div>
  <svg class="hero-slant" width="1200" height="90" viewBox="0 0 1200 90"><polygon points="0,20 1200,90 0,90" fill="#fff"/><polygon points="0,90 1200,40 1200,90" fill="#fff" opacity=".6"/></svg>
</section>

<section class="about">
  <h2 class="section-title">About</h2>
  <p class="lead">Corbel Strategy Partners is a boutique management consulting firm based in Sydney that helps small and mid sized enterprises. We are experts in business and performance improvement, process optimisation, profit maximisation and regulation compliance. Our team has many years of experience providing support to companies operating in a variety of different industries and helps our clients make lasting improvements to their performance and realise their most important goals.</p>
</section>

<section class="services">
  <svg class="services-arrow" style="left:20px" width="14" height="24" viewBox="0 0 14 24"><polyline points="11,3 3,12 11,21" fill="none" stroke="#757575" stroke-width="2"/></svg>
  <svg class="services-arrow" style="right:20px" width="14" height="24" viewBox="0 0 14 24"><polyline points="3,3 11,12 3,21" fill="none" stroke="#757575" stroke-width="2"/></svg>
  <h2 class="section-title">Our Services</h2>
  <p class="lead">Our experience spreads through providing a broad range of assistance from different industries and an array that enables the firm to assist clients achieve successfully as a result of the best way to improve your business performance.</p>
  <div class="service-list">
    <div class="service">
      <div class="service-icon active"><svg width="34" height="34" viewBox="0 0 34 34"><polyline points="3,18 10,18 13,10 18,26 21,16 31,16" fill="none" stroke="#fff" stroke-width="2.5"/></svg></div>
      <h3>Business Health Checks</h3>
      <p>Corbel Strategy Partners provides a flexible health check for your business. We will review your overall performance.</p>
    </div>
    <div class="service">
      <div class="service-icon"><svg width="34" height="34" viewBox="0 0 34 34"><rect x="5" y="18" width="5" height="11" fill="#1c3553"/><rect x="14" y="12" width="5" height="17" fill="#1c3553"/><rect x="23" y="6" width="5" height="23" fill="#1c3553"/></svg></div>
      <h3>Business Performance</h3>
      <p>Corbel Strategy Partners helps you find the levers that lift results. We will measure and improve what matters.</p>
    </div>
    <div class="service">
      <div class="service-icon"><svg width="34" height="34" viewBox="0 0 34 34"><path d="M27 12a11 11 0 1 0 1 9" fill="none" stroke="#1c3553" stroke-width="2.5"/><polyline points="28,5 28,13 20,13" fill="none" stroke="#1c3553" stroke-width="2.5"/></svg></div>
      <h3>Turnaround Management</h3>
      <p>Corbel Strategy Partners guides firms through difficult periods. We will stabilise cash flow and chart recovery.</p>
    </div>
    <div class="service">
      <div class="service-icon"><svg width="34" height="34" viewBox="0 0 34 34"><circle cx="17" cy="11" r="6" fill="#1c3553"/><path d="M6 30c1-8 6-11 11-11s10 3 11 11z" fill="#1c3553"/></svg></div>
      <h3>Independent Insolvency</h3>
      <p>Corbel Strategy Partners offers clear independent advice. We will review your options and next steps.</p>
    </div>
  </div>
</section>

<section class="news-links">
  <div class="news">
    <h2 class="col-title">Latest News</h2>
    <div class="news-item">
      <h4>Tax Appointment</h4>
      <p>When a business encounters difficult financial circumstances, it can be a very stressful time for business owners and suppliers alike.</p>
      <div class="more">More</div>
    </div>
    <div class="news-item">
      <h4>Tax Appointment</h4>
      <p>When a business encounters difficult financial circumstances, it can be a very stressful time for business owners and suppliers alike.</p>
      <div class="more">More</div>
    </div>
  </div>
  <div class="links">
    <h2 class="col-title">Links</h2>
    <h4>Regulatory and compliance links</h4>
    <div class="link-row"><span>www.revenue.example</span>– National Revenue Office</div>
    <div class="link-row"><span>www.registry.example</span>– Corporate Registry Commission</div>
    <div class="link-row"><span>www.enterprise.example</span>– Enterprise Support Portal</div>
    <div class="link-row"><span>www.solvency.example</span>– Restructuring and Solvency Service</div>
    <div class="link-row"><span>www.accountants.example</span>– Chartered Accountants Institute</div>
    <div class="link-row"><span>www.turnaround.example</span>– Turnaround Practitioners Association</div>
  </div>
</section>

<section class="team">
  <h2 class="section-title">Our Team</h2>
  <p class="lead">Our experience spreads through providing a broad range of assistance from different industries and an array.</p>
  <div class="team-list">
    <div class="member">
      <div class="member-photo" role="img" aria-label="Portrait of a team member in a business suit" style="background:linear-gradient(135deg,#8ea4b8,#5f6f7e)"></div>
      <h3>Corbel Strategy</h3>
      <p>When a business encounters difficult financial circumstances, it can be a very stressful time for business owners and suppliers alike.</p>
      <div class="social"><span></span><span></span><span class="mail"><svg width="12" height="9" viewBox="0 0 12 9"><rect x=".5" y=".5" width="11" height="8" fill="none" stroke="#fff"/><polyline points=".5,.5 6,5 11.5,.5" fill="none" stroke="#fff"/></svg></span></div>
    </div>
    <div class="member">
      <div class="member-photo" role="img" aria-label="Portrait of a team member at an office desk" style="background:linear-gradient(135deg,#c9b9a6,#7d7468)"></div>
      <h3>Corbel Strategy</h3>
      <p>When a business encounters difficult financial circumstances, it can be a very stressful time for business owners and suppliers alike.</p>
      <div class="social"><span></span><span></span><span class="mail"><svg width="12" height="9" viewBox="0 0 12 9"><rect x=".5" y=".5" width="11" height="8" fill="none" stroke="#fff"/><polyline points=".5,.5 6,5 11.5,.5" fill="none" stroke="#fff"/></svg></span></div>
    </div>
    <div class="member">
      <div class="member-photo" role="img" aria-label="Portrait of a team member in a bright office" style="background:linear-gradient(135deg,#e4e6e2,#a3a9a0)"></div>
      <h3>Corbel Strategy</h3>
      <p>When a business encounters difficult financial circumstances, it can be a very stressful time for business owners and suppliers alike.</p>
      <div class="social"><span></span><span></span><span class="mail"><svg width="12" height="9" viewBox="0 0 12 9"><rect x=".5" y=".5" width="11" height="8" fill="none" stroke="#fff"/><polyline points=".5,.5 6,5 11.5,.5" fill="none" stroke="#fff"/></svg></span></div>
    </div>
  </div>
</section>

<section class="contact">
  <h2 class="section-title">Contact Us</h2>
  <div class="contact-details">Level 10, 52 Harbour Lane Sydney NSW 2000 Australia<br>Call: (02) 9000 4821 &nbsp; Email: hello@corbelstrategy.example</div>
  <div class="contact-form">
    <div class="field-message">Message</div>
    <div class="fields">
      <div class="field">Name</div>
      <div class="field">Email</div>
      <div class="field-row"><div class="field">Type the code shown</div><div class="btn-submit">SUBMIT</div></div>
    </div>
  </div>
</section>

<footer class="site-footer">
  <div class="to-top"><svg width="14" height="10" viewBox="0 0 14 10"><polyline points="2,8 7,3 12,8" fill="none" stroke="#fff" stroke-width="2.5"/></svg></div>
  <p class="copyright">Copyright © 2015 <b>Corbel Strategy Partners</b>. All rights reserved.</p>
</footer>

</body>
</html>
```